Retractable Banners Designs for Tradeshows

We like the look and feel of the banners draft but want a more polished and improved version of the banners

The dimensions of each banner should be 33" x 80"

We want the banners to work on their own as they will be used in different places, but at tradeshows, they might be used side by side in a 10x10 tradeshow booth, so common design elements that work together is needed.
Updates

Low design quality

Target Market(s)

tradeshows booths

Colors
EB3D1F
EC4F4E
F09395
F8D3D4
FCEDEE

Requirements
Must have
• Elements that tie all the banners together, large scale images, not to cluttered or busy, designed to be visible and attractive from far away, our corporate colours are red, black, white and gray
Nice to have
• bright design not dark but using our corporate colours of red, gray, white and some black

```html
<!DOCTYPE html>
<html lang="en">
<head>
<meta charset="utf-8">
<title>Relaywave Tradeshow Banners</title>
<link href="https://fonts.googleapis.com/css2?family=Ubuntu:wght@300;400;700&display=swap" rel="stylesheet">
<style>
  :root {
    --red: #d8202d;
    --red-deep: #b51a25;
    --red-bright: #eb3d3f;
    --charcoal: #3b3e44;
    --charcoal-dark: #2a2c30;
    --white: #ffffff;
    --stage: #e9eaec;
  }
  * { margin: 0; padding: 0; box-sizing: border-box; }
  html, body { width: 1200px; height: 792px; overflow: hidden; }
  body {
    background: var(--stage);
    font-family: "Ubuntu", sans-serif;
    display: flex;
    align-items: center;
    justify-content: center;
  }
  .banner-set { display: flex; gap: 6px; }
  .banner {
    position: relative;
    width: 290px;
    height: 703px;
    overflow: hidden;
    background: var(--red);
  }
  .banner__photo {
    position: absolute;
    left: 0; top: 0;
    width: 100%;
    height: 520px;
  }
  .photo--towers { background: linear-gradient(175deg, #2e5fb8 0%, #4b7fd0 45%, #7d8fa6 80%, #3a3d44 100%); }
  .photo--racks  { background: linear-gradient(180deg, #8c9096 0%, #4a4e55 40%, #2f3237 100%); }
  .photo--bench  { background: linear-gradient(180deg, #6f6f6c 0%, #8a877f 40%, #3c3e42 100%); }
  .photo--field  { background: linear-gradient(160deg, #9fa3a8 0%, #b9b6b2 35%, #8f7f7a 65%, #6e7278 100%); }
  .banner__art {
    position: absolute;
    inset: 0;
    width: 100%;
    height: 100%;
  }
  .banner__brand {
    position: absolute;
    top: 0; left: 0; right: 0;
    height: 72px;
    display: flex;
    align-items: center;
    justify-content: center;
    gap: 8px;
    padding-top: 22px;
  }
  .brand__dot {
    width: 14px; height: 14px;
    border-radius: 50%;
    background: var(--red-bright);
  }
  .brand__name {
    font-weight: 400;
    font-size: 28px;
    letter-spacing: -0.5px;
    color: var(--white);
  }
  .banner__copy {
    position: absolute;
    left: 0; right: 0;
    top: 505px; bottom: 20px;
    display: flex;
    flex-direction: column;
    align-items: center;
    justify-content: center;
    text-align: center;
    color: var(--white);
  }
  .banner__title {
    font-weight: 700;
    font-size: 25px;
    line-height: 1.1;
    letter-spacing: 0.5px;
    text-transform: uppercase;
  }
  .banner__rule {
    width: 210px;
    height: 2px;
    background: var(--white);
    margin: 10px 0 12px;
  }
  .banner__tagline {
    font-weight: 300;
    font-size: 20px;
    line-height: 1.25;
  }
</style>
</head>
<body>
<main class="banner-set">

  <section class="banner">
    <div class="banner__photo photo--towers" role="img" aria-label="Cell tower antennas against a blue sky"></div>
    <svg class="banner__art" viewBox="0 0 290 703" preserveAspectRatio="none" aria-hidden="true">
      <path d="M0 0H290V70Q150 78 0 108Z" fill="var(--charcoal)" opacity="0.85"/>
      <path d="M0 108Q150 78 290 70V92Q150 98 0 132Z" fill="var(--red)"/>
      <path d="M0 132Q150 98 290 92V122Q150 124 0 160Z" fill="var(--white)" opacity="0.75"/>
      <path d="M0 440Q150 470 290 478V703H0Z" fill="var(--red-deep)" opacity="0.85"/>
      <path d="M0 470Q150 500 290 492V703H0Z" fill="var(--red)"/>
    </svg>
    <div class="banner__brand"><span class="brand__dot"></span><span class="brand__name">relaywave</span></div>
    <div class="banner__copy">
      <h2 class="banner__title">Telecom<br>Infrastructure</h2>
      <div class="banner__rule"></div>
      <p class="banner__tagline">Cutting Edge<br>Solutions for the<br>Next Generations</p>
    </div>
  </section>

  <section class="banner">
    <div class="banner__photo photo--racks" role="img" aria-label="Server racks with network equipment in a data room"></div>
    <svg class="banner__art" viewBox="0 0 290 703" preserveAspectRatio="none" aria-hidden="true">
      <path d="M0 0H290V75Q150 72 0 75Z" fill="var(--charcoal)" opacity="0.8"/>
      <path d="M0 75Q150 72 290 75V92Q150 86 0 92Z" fill="var(--red)"/>
      <path d="M0 92Q150 86 290 92V112Q150 104 0 118Z" fill="var(--white)" opacity="0.7"/>
      <path d="M0 478Q150 470 290 478V703H0Z" fill="var(--red-deep)" opacity="0.85"/>
      <path d="M0 492Q150 496 290 500V703H0Z" fill="var(--red)"/>
    </svg>
    <div class="banner__brand"><span class="brand__dot"></span><span class="brand__name">relaywave</span></div>
    <div class="banner__copy">
      <h2 class="banner__title">ITC Solutions</h2>
      <div class="banner__rule"></div>
      <p class="banner__tagline">Seamless Cable and<br>Telecom Networks<br>and Enterprise<br>Deployments</p>
    </div>
  </section>

  <section class="banner">
    <div class="banner__photo photo--bench" role="img" aria-label="Signal generators and measurement instruments on a lab shelf"></div>
    <svg class="banner__art" viewBox="0 0 290 703" preserveAspectRatio="none" aria-hidden="true">
      <path d="M0 0H290V75Q150 72 0 75Z" fill="var(--charcoal-dark)" opacity="0.85"/>
      <path d="M0 75Q150 72 290 82V92Q150 84 0 85Z" fill="var(--red)"/>
      <path d="M0 85Q150 84 290 92V98Q150 92 0 92Z" fill="var(--white)" opacity="0.7"/>
      <path d="M0 478Q150 492 290 488V703H0Z" fill="var(--red-deep)" opacity="0.85"/>
      <path d="M0 500Q150 510 290 494V703H0Z" fill="var(--red)"/>
    </svg>
    <div class="banner__brand"><span class="brand__dot"></span><span class="brand__name">relaywave</span></div>
    <div class="banner__copy">
      <h2 class="banner__title">Test &amp;<br>Measurement</h2>
      <div class="banner__rule"></div>
      <p class="banner__tagline">Accurate and<br>Efficient Solutions<br>for the Wireless<br>World</p>
    </div>
  </section>

  <section class="banner">
    <div class="banner__photo photo--field" role="img" aria-label="Technician in a hard hat installing a radio unit on a tower"></div>
    <svg class="banner__art" viewBox="0 0 290 703" preserveAspectRatio="none" aria-hidden="true">
      <path d="M0 0H290V84Q150 78 0 75Z" fill="var(--charcoal)" opacity="0.85"/>
      <path d="M0 75Q150 78 290 84V95Q150 86 0 84Z" fill="var(--red)"/>
      <path d="M0 84Q150 86 290 95V100Q150 92 0 90Z" fill="var(--white)" opacity="0.7"/>
      <path d="M0 430Q150 420 290 370V440Q150 470 0 470Z" fill="var(--white)" opacity="0.9"/>
      <path d="M0 470Q150 470 290 440V703H0Z" fill="var(--red-deep)" opacity="0.85"/>
      <path d="M0 494Q150 492 290 478V703H0Z" fill="var(--red)"/>
    </svg>
    <div class="banner__brand"><span class="brand__dot"></span><span class="brand__name">relaywave</span></div>
    <div class="banner__copy">
      <h2 class="banner__title">Hardware</h2>
      <div class="banner__rule"></div>
      <p class="banner__tagline">High-Quality,<br>Economical, Test<br>Grade RF and<br>Microwave Components</p>
    </div>
  </section>

</main>
</body>
</html>
```